Meadow Reset sale graphics for social media

You MUST read the Brief in the WORD document and follow the instructions there. I want to create 10 social media graphics (new Instagram size 4:5 (1080 x 1350 pixels) focusing on our Mother’s Day Meadow Reset Sale graphics, using any of the pics attached. Use the attached pics, NO RANDOM STOCK PHOTOGRAPHY. For the color scheme of the graphics, they should all be complementary to the product colors or feel like Spring time.

Target Market(s)

primarily women

Requirements
Must have
• the photos and text attached

```html
<!DOCTYPE html>
<html lang="en">
<head>
<meta charset="utf-8">
<title>Meadow Reset Mother's Day Sale – Social Set</title>
<link rel="stylesheet" href="https://fonts.googleapis.com/css2?family=Playfair+Display:ital,wght@0,900;1,800;1,900&family=Archivo+Black&family=DM+Sans:wght@500;700&display=swap">
<style>
  :root {
    --plum: #63284b;
    --pink-light: #f6dcec;
    --pink-mid: #f0c3de;
    --pink-deep: #e39ac6;
    --pink-accent: #f2a7d6;
    --white: #ffffff;
    --bottle: #f4f3f1;
    --bottle-shade: #d9d6d3;
  }
  * { box-sizing: border-box; margin: 0; padding: 0; }
  html, body { width: 1200px; height: 608px; overflow: hidden; background: var(--white); }
  .sheet { position: relative; width: 1200px; height: 608px; }
  .post {
    position: absolute; width: 227px; height: 284px; overflow: hidden;
    background: linear-gradient(180deg, var(--pink-mid) 0%, var(--pink-light) 55%, var(--pink-deep) 100%);
    color: var(--plum);
  }
  .burst { position: absolute; left: 22px; top: 16px; width: 184px; height: 160px; }
  .bottle {
    position: absolute; z-index: 1; border-radius: 4px 4px 3px 3px;
    background: linear-gradient(90deg, var(--bottle-shade), var(--bottle) 45%, var(--bottle-shade));
    box-shadow: 0 1px 2px rgba(0,0,0,.2);
  }
  .bottle-top   { left: 118px; top: 6px;   width: 20px; height: 32px; transform: rotate(10deg); }
  .bottle-side  { left: 193px; top: 86px;  width: 11px; height: 20px; transform: rotate(-8deg); }
  .bottle-left  { left: 42px;  top: 124px; width: 17px; height: 30px; transform: rotate(22deg); }
  .bottle-right { left: 152px; top: 134px; width: 20px; height: 32px; transform: rotate(-30deg); }
  .line {
    position: absolute; z-index: 2; left: 0; right: 0; text-align: center;
    transform: translateY(-50%); white-space: nowrap; line-height: 1;
  }
  .pct { font-family: "Playfair Display", serif; font-weight: 900; font-size: 68px; color: var(--white); letter-spacing: -1px; }
  .off { font-family: "Playfair Display", serif; font-style: italic; font-weight: 900; font-size: 28px; color: var(--pink-accent); }
  .script { font-family: "Playfair Display", serif; font-style: italic; font-weight: 900; letter-spacing: -1px; }
  .sans { font-family: "DM Sans", sans-serif; font-weight: 700; }
  .block { font-family: "Archivo Black", sans-serif; letter-spacing: -1px; }
</style>
</head>
<body>
<svg width="0" height="0" style="position:absolute" aria-hidden="true">
  <symbol id="burst-shape" viewBox="0 0 184 160">
    <ellipse cx="92" cy="82" rx="80" ry="68" fill="#63284b" stroke="#63284b" stroke-width="9" stroke-dasharray="5 4"/>
  </symbol>
</svg>

<main class="sheet">

  <!-- Row 1 -->
  <section class="post" style="left:14px;top:16px">
    <svg class="burst"><use href="#burst-shape"/></svg>
    <div class="bottle bottle-top" role="img" aria-label="Supplement bottle"></div>
    <div class="bottle bottle-side" role="img" aria-label="Supplement bottle"></div>
    <div class="bottle bottle-left" role="img" aria-label="Supplement bottle"></div>
    <div class="bottle bottle-right" role="img" aria-label="Supplement bottle"></div>
    <div class="line script" style="top:76px;font-size:34px;color:var(--pink-accent)">Mother’s</div>
    <div class="line script" style="top:110px;font-size:34px;color:var(--pink-accent)">Day</div>
    <div class="line script" style="top:202px;font-size:54px">Meadow</div>
    <div class="line sans" style="top:242px;font-size:14px">RESET SALE</div>
    <div class="line sans" style="top:258px;font-size:14px">25% Off Everything!</div>
  </section>

  <section class="post" style="left:250px;top:16px">
    <svg class="burst"><use href="#burst-shape"/></svg>
    <div class="bottle bottle-top" role="img" aria-label="Supplement bottle"></div>
    <div class="bottle bottle-side" role="img" aria-label="Supplement bottle"></div>
    <div class="bottle bottle-left" role="img" aria-label="Supplement bottle"></div>
    <div class="bottle bottle-right" role="img" aria-label="Supplement bottle"></div>
    <div class="line pct" style="top:84px">25%</div>
    <div class="line off" style="top:134px">off</div>
    <div class="line sans" style="top:188px;font-size:14px;font-weight:500">Mother’s Day Sale</div>
    <div class="line script" style="top:222px;font-size:52px">Refresh</div>
    <div class="line script" style="top:262px;font-size:24px;font-weight:800">Your Body</div>
  </section>

  <section class="post" style="left:486px;top:16px">
    <svg class="burst"><use href="#burst-shape"/></svg>
    <div class="bottle bottle-top" role="img" aria-label="Supplement bottle"></div>
    <div class="bottle bottle-side" role="img" aria-label="Supplement bottle"></div>
    <div class="bottle bottle-left" role="img" aria-label="Supplement bottle"></div>
    <div class="bottle bottle-right" role="img" aria-label="Supplement bottle"></div>
    <div class="line pct" style="top:84px">25%</div>
    <div class="line off" style="top:134px">off</div>
    <div class="line script" style="top:196px;font-size:34px">Meadow</div>
    <div class="line script" style="top:232px;font-size:34px">Reset Sale</div>
    <div class="line sans" style="top:266px;font-size:11px;font-weight:500">This Spring Shine like SUMMER</div>
  </section>

  <section class="post" style="left:722px;top:16px">
    <svg class="burst"><use href="#burst-shape"/></svg>
    <div class="bottle bottle-top" role="img" aria-label="Supplement bottle"></div>
    <div class="bottle bottle-side" role="img" aria-label="Supplement bottle"></div>
    <div class="bottle bottle-left" role="img" aria-label="Supplement bottle"></div>
    <div class="bottle bottle-right" role="img" aria-label="Supplement bottle"></div>
    <div class="line pct" style="top:84px">25%</div>
    <div class="line off" style="top:134px">off</div>
    <div class="line script" style="top:190px;font-size:31px">Mother’s Day</div>
    <div class="line block" style="top:232px;font-size:64px">SALE</div>
    <div class="line sans" style="top:269px;font-size:10px">Detox this SUMMER. Shine this SUMMER</div>
  </section>

  <section class="post" style="left:958px;top:16px">
    <svg class="burst"><use href="#burst-shape"/></svg>
    <div class="bottle bottle-top" role="img" aria-label="Supplement bottle"></div>
    <div class="bottle bottle-side" role="img" aria-label="Supplement bottle"></div>
    <div class="bottle bottle-left" role="img" aria-label="Supplement bottle"></div>
    <div class="bottle bottle-right" role="img" aria-label="Supplement bottle"></div>
    <div class="line pct" style="top:84px">25%</div>
    <div class="line off" style="top:134px">off</div>
    <div class="line script" style="top:194px;font-size:24px">Mother’s Day Sale</div>
    <div class="line block" style="top:225px;font-size:36px">MEADOW</div>
    <div class="line sans" style="top:256px;font-size:12px;font-weight:500">—— Reset for a Summer Body ——</div>
  </section>

  <!-- Row 2 -->
  <section class="post" style="left:14px;top:308px">
    <svg class="burst"><use href="#burst-shape"/></svg>
    <div class="bottle bottle-top" role="img" aria-label="Supplement bottle"></div>
    <div class="bottle bottle-side" role="img" aria-label="Supplement bottle"></div>
    <div class="bottle bottle-left" role="img" aria-label="Supplement bottle"></div>
    <div class="bottle bottle-right" role="img" aria-label="Supplement bottle"></div>
    <div class="line pct" style="top:84px">25%</div>
    <div class="line off" style="top:134px">off</div>
    <div class="line script" style="top:192px;font-size:31px">Mother’s Day</div>
    <div class="line sans" style="top:223px;font-size:23px;letter-spacing:-.5px">MEADOW RESET</div>
    <div class="line block" style="top:257px;font-size:42px;letter-spacing:6px">SALE</div>
  </section>

  <section class="post" style="left:250px;top:308px">
    <svg class="burst"><use href="#burst-shape"/></svg>
    <div class="bottle bottle-top" role="img" aria-label="Supplement bottle"></div>
    <div class="bottle bottle-side" role="img" aria-label="Supplement bottle"></div>
    <div class="bottle bottle-left" role="img" aria-label="Supplement bottle"></div>
    <div class="bottle bottle-right" role="img" aria-label="Supplement bottle"></div>
    <div class="line pct" style="top:84px">25%</div>
    <div class="line off" style="top:134px">off</div>
    <div class="line sans" style="top:186px;font-size:14px;font-weight:500">All Supplements</div>
    <div class="line script" style="top:222px;font-size:50px">Meadow</div>
    <div class="line sans" style="top:263px;font-size:13px;font-weight:500">RESET SALE</div>
  </section>

  <section class="post" style="left:486px;top:308px">
    <svg class="burst"><use href="#burst-shape"/></svg>
    <div class="bottle bottle-top" role="img" aria-label="Supplement bottle"></div>
    <div class="bottle bottle-side" role="img" aria-label="Supplement bottle"></div>
    <div class="bottle bottle-left" role="img" aria-label="Supplement bottle"></div>
    <div class="bottle bottle-right" role="img" aria-label="Supplement bottle"></div>
    <div class="line pct" style="top:84px">25%</div>
    <div class="line off" style="top:134px">off</div>
    <div class="line sans" style="top:186px;font-size:17px">— MEADOW RESET —</div>
    <div class="line block" style="top:227px;font-size:64px">SALE</div>
    <div class="line sans" style="top:266px;font-size:13px;font-weight:500">Spring Reset. Summer Ready.</div>
  </section>

  <section class="post" style="left:722px;top:308px">
    <svg class="burst"><use href="#burst-shape"/></svg>
    <div class="bottle bottle-top" role="img" aria-label="Supplement bottle"></div>
    <div class="bottle bottle-side" role="img" aria-label="Supplement bottle"></div>
    <div class="bottle bottle-left" role="img" aria-label="Supplement bottle" style="left:36px;top:130px"></div>
    <div class="bottle bottle-right" role="img" aria-label="Supplement bottle" style="left:156px;top:136px"></div>
    <div class="line pct" style="top:80px;font-size:60px">25%</div>
    <div class="line off" style="top:119px;font-size:16px">off everything</div>
    <div class="line sans" style="top:190px;font-size:18px">MOTHER’S DAY</div>
    <div class="line block" style="top:222px;font-size:36px">MEADOW</div>
    <div class="line script" style="top:257px;font-size:28px">Reset Sale</div>
  </section>

  <section class="post" style="left:958px;top:308px">
    <svg class="burst"><use href="#burst-shape"/></svg>
    <div class="bottle bottle-top" role="img" aria-label="Supplement bottle"></div>
    <div class="bottle bottle-side" role="img" aria-label="Supplement bottle"></div>
    <div class="bottle bottle-left" role="img" aria-label="Supplement bottle"></div>
    <div class="bottle bottle-right" role="img" aria-label="Supplement bottle"></div>
    <div class="line pct" style="top:84px">25%</div>
    <div class="line off" style="top:134px">off</div>
    <div class="line script" style="top:194px;font-size:36px">Mother’s</div>
    <div class="line script" style="top:229px;font-size:36px">Day Sale</div>
    <div class="line sans" style="top:266px;font-size:14px;font-weight:500">Feel Amazing Again</div>
  </section>

</main>
</body>
</html>
```